New packaging company website**

We are looking for a new design for our corporate website (www.borvellotrade.it). The theme must be made with Elementor and Crocoblock plugins. Currently the demo site can be reached at www.borvellotrade.cloud

You can also check our current site for your reference www.borvellotrade.it
We mainly deal with the resale of industrial containers for companies, most of our customers are B2B but also a good number of private customers. The site must therefore be accessible to all and the prices always visible even without registration or other.

Given the heterogeneity of our articles, we need a very clear shop page, with clearly visible filters and possibly with a list view and a table.

However, it does not have to be a simple ecommerce, we still want a site with many texts, spaces for product FAQs, tooltips on filters or attributes.

Target Market(s)

90% B2B

Coding

Coded - Design and coding required

Requirements
Must have
• beautiful, modern and captivating graphics. It must be a "full" site and not a flat one.
Nice to have
• We are undecided about the location of the main product menu.

If you leave the top bar with the icons and labels of the macro categories, as happens now on the live site and on the demo site.

Or if you want to insert the classic "all categories" on the top menu (https://fernalux.qorvidex.com/demo-tools/demo/tools/ or https://www.velmiratheme.com/wordpress/velmira/shop30/)

Or if you want to take advantage of something more modern, such as the sidebar menu (https://www.velmiratheme.com/wordpress/velmira/shop10/ or https://www.velmiratheme.com/wordpress/velmira/shop19/)

```html
<!DOCTYPE html>
<html lang="it">
<head>
<meta charset="utf-8">
<title>Borvello Trade – Forniture per enti e aziende</title>
<link href="https://fonts.googleapis.com/css2?family=Bebas+Neue&family=Poppins:wght@400;500;600;700&display=swap" rel="stylesheet">
<style>
:root{
  --blue:#0b4f8a;
  --blue-dark:#0a3f70;
  --red:#d6282c;
  --yellow:#ffd800;
  --green:#2e9e3a;
  --ink:#1b1b1b;
  --muted:#666;
  --price:#d32f2f;
  --card:#f4f4f4;
  --footer:#efefef;
}
*{margin:0;padding:0;box-sizing:border-box}
html,body{width:1200px;height:3131px;overflow:hidden}
body{position:relative;background:#fff;font-family:"Poppins",sans-serif;color:var(--ink)}
.abs{position:absolute}
.display{font-family:"Bebas Neue",sans-serif;font-weight:400;letter-spacing:.2px}

.topbar{left:0;top:0;width:1200px;height:34px;background:var(--blue);color:#fff;font-size:12px;font-weight:500}
.topbar .promo{left:88px;top:9px}
.topbar .contacts{right:88px;top:9px;display:flex;gap:18px;align-items:center}
.topbar .contacts span{display:flex;align-items:center;gap:5px}

.sidebar{left:0;top:34px;width:63px;height:653px;background:var(--blue);z-index:3}
.sidebar svg{position:absolute;left:19px;width:25px;height:25px}

.hero{left:63px;top:34px;width:1137px;height:654px;background:linear-gradient(180deg,#fafafa,#ececec)}
.header{left:63px;top:34px;width:1137px;height:70px}
.logo{left:26px;top:16px;display:flex;align-items:center;gap:8px}
.logo .mark{width:26px;height:26px;background:var(--green)}
.logo .name{font-size:22px;font-weight:700;color:var(--blue);letter-spacing:1px}
.nav{left:458px;top:27px;display:flex;gap:28px;font-size:13.5px;font-weight:600}
.tools{left:950px;top:22px;display:flex;gap:10px;align-items:center}
.badge-count{position:absolute;right:-6px;top:-4px;width:11px;height:11px;border-radius:50%;background:var(--yellow);font-size:7px;text-align:center;line-height:11px;font-weight:700}

.hero-title{left:128px;top:236px;color:var(--blue);font-size:100px;line-height:85px}
.hero-title .accent{color:var(--red)}
.hero-sub{left:128px;top:418px;font-size:41px;color:#222}
.btn-yellow{left:129px;top:467px;width:205px;height:32px;background:var(--yellow);font-size:13px;font-weight:700;text-align:center;line-height:32px}
.hero-img{left:553px;top:219px;width:554px;height:316px;border-radius:30px 30px 12px 12px;background:linear-gradient(90deg,#9aa3ad 0%,#2f6fd0 22%,#b8bcc2 40%,#f1c400 58%,#e0232a 75%,#a8adb3 100%)}
.dots{left:575px;top:619px;display:flex;gap:8px}
.dots i{width:11px;height:11px;border-radius:50%;background:#999;display:block}
.dots i.on{background:var(--blue)}

.section-title{left:89px;font-size:40px;color:var(--ink)}
.btn-view{left:1003px;width:107px;height:36px;background:var(--blue);color:#fff;font-size:14px;font-weight:700;text-align:center;line-height:36px;letter-spacing:.5px}

.products{left:89px;width:1024px;display:flex;gap:7px}
.product{width:165px}
.product .thumb{position:relative;height:195px;background:var(--card)}
.product .thumb .img{position:absolute;left:32px;top:40px;width:100px;height:115px;border-radius:8px}
.product .sale{position:absolute;left:20px;top:20px;background:var(--green);color:#fff;font-size:7.5px;font-weight:700;padding:2px 5px}
.product .name{margin-top:13px;font-size:11px;font-weight:500;line-height:15px;height:45px;overflow:hidden}
.product .price{margin-top:3px;font-size:13.5px;font-weight:700;color:var(--price)}

.banner{width:509px;height:180px;overflow:hidden}
.banner .pic{position:absolute;right:0;top:0;width:260px;height:180px}
.banner .eyebrow{position:absolute;left:48px;top:58px;font-size:19px}
.banner .big{position:absolute;left:48px;top:74px;font-size:55px;line-height:55px}
.banner .more{position:absolute;left:48px;top:128px;font-size:13px;font-weight:700;color:var(--yellow)}

.feature{width:240px;text-align:center}
.feature svg{width:76px;height:50px}
.feature h3{font-size:21px;margin-top:18px}
.feature p{font-size:12px;color:var(--muted);line-height:17px;margin-top:2px}
.rule{left:89px;top:2180px;width:1021px;height:1px;background:#ddd}

.about-img{left:89px;top:2248px;width:467px;height:282px;background:linear-gradient(90deg,#1763c0 0%,#2a7be0 45%,#f4c400 55%,#ffd400 100%)}
.about-title{left:598px;top:2296px;font-size:41px;line-height:42px}
.about-text{left:598px;top:2398px;width:520px;font-size:14.5px;line-height:24.5px;color:#333}

.newsletter{left:89px;top:2598px;width:1111px;height:170px;background:var(--yellow)}
.newsletter h2{position:absolute;left:44px;top:57px;font-size:41px;line-height:40px}
.newsletter p{position:absolute;left:44px;top:96px;width:480px;font-size:14px;line-height:18px}
.newsletter .field{position:absolute;left:549px;top:69px;width:371px;height:42px;background:#fff;font-size:14px;color:#777;padding-left:20px;line-height:42px}
.newsletter .send{position:absolute;left:920px;top:69px;width:101px;height:42px;background:#111;color:#fff;font-size:15px;font-weight:700;text-align:center;line-height:42px}

.footer{left:89px;top:2768px;width:1111px;height:363px;background:var(--footer)}
.footer h4{font-size:23px;line-height:24px;margin-bottom:6px}
.footer .col{position:absolute;top:92px;font-size:13px;color:#555;line-height:23px}
.footer .about{font-size:13px;line-height:19px;width:330px}
.footer .about .upper{font-size:12px;margin-bottom:0}
.footer .bottom{position:absolute;left:48px;top:321px;width:973px;border-top:1px solid #ccc}
.footer .copy{position:absolute;left:48px;top:335px;font-size:12px;font-weight:600;color:#333}
.footer .social{position:absolute;left:933px;top:338px;display:flex;gap:10px}
.footer .social i{display:block;width:10px;height:10px;border-radius:50%;background:#222}
</style>
</head>
<body>

<div class="abs topbar">
  <div class="abs promo">Prodotti COVID-19 in pronta consegna SCONTI FINO al 70%</div>
  <div class="abs contacts">
    <span><svg width="12" height="12" viewBox="0 0 24 24"><path fill="#ffd800" d="M6.6 10.8a15 15 0 0 0 6.6 6.6l2.2-2.2c.3-.3.7-.4 1-.2 1.1.4 2.3.6 3.6.6.6 0 1 .4 1 1V20c0 .6-.4 1-1 1A17 17 0 0 1 3 4c0-.6.4-1 1-1h3.5c.6 0 1 .4 1 1 0 1.3.2 2.5.6 3.6.1.3 0 .7-.2 1z"/></svg>02 55310420</span>
    <span><svg width="12" height="10" viewBox="0 0 24 18"><rect width="24" height="18" rx="2" fill="#ffd800"/><path d="M1 1l11 9 11-9" stroke="#0b4f8a" stroke-width="2" fill="none"/></svg>info@borvellotrade.it</span>
    <span><svg width="11" height="12" viewBox="0 0 22 24"><circle cx="11" cy="7" r="6" fill="#ffd800"/><path d="M0 24c0-7 5-10 11-10s11 3 11 10z" fill="#ffd800"/></svg>Login</span>
  </div>
</div>

<nav class="abs sidebar" aria-label="Categorie">
  <svg style="top:39px" viewBox="0 0 24 24"><path fill="#fff" d="M2 2h6v6H2zM9 2h6v6H9zM16 2h6v6h-6zM2 9h6v6H2zM9 9h6v6H9zM16 9h6v6h-6zM2 16h6v6H2zM9 16h6v6H9zM16 16h6v6h-6z"/></svg>
  <svg style="top:120px" viewBox="0 0 24 24"><rect x="5" y="2" width="14" height="20" rx="2" fill="#fff"/><path d="M5 8h14M5 14h14" stroke="#0b4f8a" stroke-width="2"/></svg>
  <svg style="top:202px" viewBox="0 0 24 24"><path fill="#fff" d="M4 5h16l-2 17H6zM9 2h6v2H9z"/><circle cx="12" cy="13" r="3" fill="#0b4f8a"/></svg>
  <svg style="top:282px" viewBox="0 0 24 24"><path fill="#fff" d="M2 12l10-6 10 6-10 6z"/><path d="M2 15l10 6 10-6" stroke="#fff" stroke-width="2" fill="none"/></svg>
  <svg style="top:364px" viewBox="0 0 24 24"><rect x="3" y="2" width="8" height="20" fill="#fff"/><rect x="13" y="2" width="8" height="20" fill="#fff"/></svg>
  <svg style="top:445px" viewBox="0 0 24 24"><rect x="2" y="6" width="20" height="15" rx="2" fill="#fff"/><rect x="8" y="3" width="8" height="4" fill="#fff"/><path d="M12 9v9M7.5 13.5h9" stroke="#0b4f8a" stroke-width="2.5"/></svg>
  <svg style="top:525px" viewBox="0 0 24 24"><path fill="#fff" d="M3 17a9 9 0 0 1 18 0zM1 18h22v3H1z"/></svg>
  <svg style="top:607px" viewBox="0 0 24 24"><circle cx="9" cy="14" r="7" fill="#fff"/><circle cx="16" cy="10" r="6" fill="none" stroke="#fff" stroke-width="2"/></svg>
</nav>

<section class="abs hero">
</section>
<header class="abs header">
  <div class="abs logo"><span class="mark"></span><span class="name">BORVELLO TRADE</span></div>
  <div class="abs nav"><span>SHOP</span><span>CHI SIAMO</span><span>CONTACTS</span><span>BLOG</span><span>SERVIZI</span><span>REGALI</span></div>
  <div class="abs tools">
    <svg width="28" height="24" viewBox="0 0 28 24"><path d="M14 2v20M6 22h16M3 6h22M3 6l-3 8h6zM25 6l-3 8h6z" stroke="#888" stroke-width="2" fill="none"/></svg>
    <svg width="26" height="24" viewBox="0 0 24 22"><path fill="#888" d="M12 21l-1.5-1.3C5 15 2 12 2 8a5 5 0 0 1 10-2 5 5 0 0 1 10 2c0 4-3 7-8.5 11.7z"/></svg>
    <span style="position:relative"><svg width="24" height="24" viewBox="0 0 24 24"><path fill="#0b4f8a" d="M1 2h4l1 3h16l-3 9H8l-1 2h13v2H4l2.5-4L4 4H1z"/><circle cx="8" cy="21" r="2" fill="#0b4f8a"/><circle cx="18" cy="21" r="2" fill="#0b4f8a"/></svg><span class="badge-count">0</span></span>
  </div>
</header>

<h1 class="abs hero-title display">FUSTI<br>IN <span class="accent">METALLO</span></h1>
<div class="abs hero-sub display">BIDONI E FUSTI IN FERRO...</div>
<div class="abs btn-yellow">VEDI TUTTA LA GAMMA</div>
<div class="abs hero-img" role="img" aria-label="Taniche e fusti in metallo e plastica colorati"></div>
<div class="abs dots"><i></i><i class="on"></i><i></i></div>

<h2 class="abs section-title display" style="top:755px">FEATURED PRODUCTS</h2>
<div class="abs btn-view" style="top:758px">VIEW ALL</div>
<div class="abs products" style="top:812px">
  <div class="product"><div class="thumb"><span class="sale">SCONTO 40%</span><div class="img" role="img" aria-label="Tanica di gel igienizzante" style="background:#e6e6e0"></div></div><div class="name">Gel igienizzante mani antisettico, 60% di alcol, in tanica da 10 Lt...</div><div class="price">€66,70</div></div>
  <div class="product"><div class="thumb"><span class="sale">SCONTO 50%</span><div class="img" role="img" aria-label="Flacone di gel igienizzante" style="background:linear-gradient(#2e9e3a 20%,#c9c6b8 20%)"></div></div><div class="name">Gel igienizzante mani antisettico, 63% di alcol, formato da 500 ml, da utilizzare...</div><div class="price">€66,70</div></div>
  <div class="product"><div class="thumb"><span class="sale">SCONTO 30%</span><div class="img" role="img" aria-label="Camice monouso bianco" style="background:#fafafa;border:1px solid #e3e3e3"></div></div><div class="name">Camice monouso da visitatore in TNT di polipropilene (PP), 30 g/mq, chiusura...</div><div class="price">€66,70</div></div>
  <div class="product"><div class="thumb"><span class="sale">SCONTO 38.2%</span><div class="img" role="img" aria-label="Trolley portautensili arancione" style="background:linear-gradient(#333 30%,#f07a1a 30%)"></div></div><div class="name">Trolley portautensili a 2 moduli sovrapponibili, Mis. 550 L x 540 P x 320 H mm</div><div class="price">€214,71</div></div>
  <div class="product"><div class="thumb"><span class="sale">SCONTO 38.2%</span><div class="img" role="img" aria-label="Pattumiere blu e grigia" style="background:linear-gradient(90deg,#1f63c6 50%,#a6a9ad 50%)"></div></div><div class="name">Pattumiere per la raccolta differenziata rifiuti, con coperchio a pressione e ...</div><div class="price">€4,16</div></div>
  <div class="product"><div class="thumb"><span class="sale">SCONTO 38.2%</span><div class="img" role="img" aria-label="Contenitori per filtri olio in acciaio" style="background:linear-gradient(90deg,#f3d600 40%,#b7b9bc 40%)"></div></div><div class="name">Contenitori raccolta filtri olio esausto, in acciaio zincato</div><div class="price">€257,66</div></div>
</div>

<div class="abs banner" style="left:89px;top:1153px;background:linear-gradient(110deg,#0d5fa8,#1b7cc9)">
  <div class="pic" role="img" aria-label="Serbatoi e cisternette in plastica blu" style="background:linear-gradient(90deg,rgba(60,160,230,0),#39a3ea 40%,#7ec4f0)"></div>
  <div class="eyebrow display" style="color:#fff">CONTENITORI IN</div>
  <div class="big display" style="color:#fff">PLASTICA</div>
  <div class="more">VEDI TUTTO &nbsp;›</div>
</div>
<div class="abs banner" style="left:606px;top:1153px;background:var(--yellow)">
  <div class="pic" role="img" aria-label="Rotoli di film estensibile" style="background:linear-gradient(90deg,rgba(255,216,0,0),#e6e6e6 50%,#222 70%,#dcdcdc)"></div>
  <div class="eyebrow display" style="color:#111">MATERIALI PER</div>
  <div class="big display" style="color:#111">L'IMBALLAGGIO</div>
  <div class="more" style="color:#111">VEDI TUTTO &nbsp;›</div>
</div>

<h2 class="abs section-title display" style="top:1396px">POPULAR PRODUCTS</h2>
<div class="abs btn-view" style="top:1399px">VIEW ALL</div>
<div class="abs products" style="top:1454px">
  <div class="product"><div class="thumb"><span class="sale">SCONTO 27.5%</span><div class="img" role="img" aria-label="Contenitore giallo per tubi al neon" style="background:linear-gradient(#b7b9bc 35%,#f3d000 35%)"></div></div><div class="name">Contenitori per la raccolta di tubi al neon esausti, in acciaio, capacità 1000 Lt</div><div class="price">€768,64</div></div>
  <div class="product"><div class="thumb"><span class="sale">SCONTO 50%</span><div class="img" role="img" aria-label="Armadio di stoccaggio zincato" style="background:#8d9aa8"></div></div><div class="name">Depositi di stoccaggio per fusti e piccoli contenitori, in acciaio zincato</div><div class="price">€1.953,40</div></div>
  <div class="product"><div class="thumb"><span class="sale">SCONTO 30%</span><div class="img" role="img" aria-label="Deposito arancione per cisternette" style="background:#ec6a1e"></div></div><div class="name">Depositi di stoccaggio per cisternette IBC 1000 Lt, in acciaio</div><div class="price">€1.988,84</div></div>
  <div class="product"><div class="thumb"><span class="sale">SCONTO 38.2%</span><div class="img" role="img" aria-label="Taniche verdi per olio esausto" style="background:#3fbf6a"></div></div><div class="name">Taniche per recupero olio esausto, in plastica (HDPE), con tappo a vite e filtro</div><div class="price">€2,00</div></div>
  <div class="product"><div class="thumb"><span class="sale">SCONTO 38.2%</span><div class="img" role="img" aria-label="Fusti blu per olio vegetale" style="background:#1d4fc2"></div></div><div class="name">Fusti per olio vegetale usato con bocchetta OlioNet, in plastica (HDPE)</div><div class="price">€171,11</div></div>
  <div class="product"><div class="thumb"><span class="sale">SCONTO 38.2%</span><div class="img" role="img" aria-label="Contenitori colorati per olio esausto" style="background:linear-gradient(90deg,#3a3d41,#2e8f3a 50%,#d6282c)"></div></div><div class="name">Contenitori per la raccolta di olio esausto, in plastica (HDPE), a doppia camera</div><div class="price">€386,67</div></div>
</div>

<div class="abs banner" style="left:89px;top:1792px;background:linear-gradient(110deg,#e2262b,#f04a44)">
  <div class="pic" role="img" aria-label="Armadio e banco da lavoro" style="background:linear-gradient(90deg,rgba(240,74,68,0),#d8dadc 45%,#2a78c6 80%)"></div>
  <div class="eyebrow display" style="color:#fff">ARREDO</div>
  <div class="big display" style="color:#fff">TECNICO</div>
  <div class="more">VEDI TUTTO &nbsp;›</div>
</div>
<div class="abs banner" style="left:606px;top:1792px;background:#2b2b2b">
  <div class="pic" role="img" aria-label="Carrello portautensili con attrezzi" style="background:linear-gradient(90deg,rgba(43,43,43,0),#e8701e 55%,#3a3a3a)"></div>
  <div class="eyebrow display" style="color:#fff">FERROX UTENSILI E</div>
  <div class="big display" style="color:#fff">ATTREZZI</div>
  <div class="more">VEDI TUTTO &nbsp;›</div>
</div>

<div class="abs feature" style="left:95px;top:2018px">
  <svg viewBox="0 0 76 50"><rect x="4" y="14" width="42" height="24" fill="none" stroke="#222" stroke-width="2.5"/><path d="M46 20h14l10 10v8H46z" fill="#ffd800" stroke="#222" stroke-width="2.5"/><circle cx="18" cy="42" r="5" fill="#fff" stroke="#222" stroke-width="2.5"/><circle cx="58" cy="42" r="5" fill="#fff" stroke="#222" stroke-width="2.5"/><circle cx="24" cy="12" r="9" fill="#ffd800" stroke="#222" stroke-width="2.5"/></svg>
  <h3 class="display">SPEDIZIONI RAPIDE</h3><p>Consegne In Tutta<br>Italia</p>
</div>
<div class="abs feature" style="left:352px;top:2018px">
  <svg viewBox="0 0 76 50"><path d="M24 28a14 14 0 0 1 28 0" fill="none" stroke="#222" stroke-width="2.5"/><rect x="20" y="26" width="8" height="14" rx="3" fill="#ffd800" stroke="#222" stroke-width="2"/><rect x="48" y="26" width="8" height="14" rx="3" fill="#ffd800" stroke="#222" stroke-width="2"/><path d="M52 40v4H40" stroke="#222" stroke-width="2" fill="none"/></svg>
  <h3 class="display">SERVIZIO CLIENTI</h3><p>Dalle 9:00 Alle 13:00<br>02/55310420</p>
</div>
<div class="abs feature" style="left:605px;top:2018px">
  <svg viewBox="0 0 76 50"><rect x="24" y="2" width="28" height="42" fill="#fff" stroke="#222" stroke-width="2.5"/><path d="M30 12h16M30 18h16M30 24h12" stroke="#222" stroke-width="2"/><circle cx="46" cy="38" r="7" fill="#ffd800" stroke="#222" stroke-width="2"/></svg>
  <h3 class="display">PRODOTTI CERTIFICATI</h3><p>Garantiti, di qualità e a<br>norma di legge</p>
</div>
<div class="abs feature" style="left:863px;top:2018px">
  <svg viewBox="0 0 76 50"><rect x="14" y="6" width="48" height="32" rx="3" fill="#fff" stroke="#222" stroke-width="2.5"/><path d="M14 14h48" stroke="#222" stroke-width="4"/><path d="M44 24l10 4v8c0 6-5 9-10 11-5-2-10-5-10-11v-8z" fill="#ffd800" stroke="#222" stroke-width="2"/></svg>
  <h3 class="display">PAGAMENTI SICURI PAYNORA</h3><p>Carte di credito, Bonifico,<br>Contrassegno</p>
</div>
<div class="abs rule"></div>

<div class="abs about-img" role="img" aria-label="Fusti metallici blu e gialli su pallet"></div>
<h2 class="abs about-title display">BORVELLOTRADE VENDITA ONLINE<br>FORNITURE PER ENTI E AZIENDE</h2>
<p class="abs about-text">Contenitori In Plastica, Contenitori in Metallo, Scaffali, Armadietti, Sicurezza &amp; Ambiente, Pallet E Bancali, prodotti per l'imballaggio, Pronto Soccorso, Antinfortunistica e DPI Consegna in 24/48H in tutta Italia. Prodotti al miglior prezzo, per il buon funzionamento<br>di ogni ente e impresa.</p>

<section class="abs newsletter">
  <h2 class="display">NEWSLETTER</h2>
  <p>Iscriviti alla nostra newsletter per restare sempre aggiornato su news e promozioni !</p>
  <div class="field">Inserisci il tuo indirizzo email</div>
  <div class="send">INVIA</div>
</section>

<footer class="abs footer">
  <div class="col about" style="left:48px">
    <h4 class="display">BORVELLO TRADE SRL</h4>
    <div class="upper">VENDITA ONLINE FORNITURE PER ENTI E AZIENDE</div>
    Contenitori In Plastica, Contenitori in Metallo, Scaffali, Armadietti, Sicurezza &amp; Ambiente, Pallet E Bancali, prodotti per l'imballaggio, Pronto Soccorso, Antinfortunistica e DPI Consegna in 24/48H in tutta Italia. Prodotti al miglior prezzo, per il buon funzionamento di ogni ente e impresa.
  </div>
  <div class="col" style="left:462px"><h4 class="display">CONTATTI</h4>Contatti<br>Chi Siamo<br>Certificazioni<br>Novità<br>Mappa del Sito</div>
  <div class="col" style="left:639px"><h4 class="display">INFORMAZIONI</h4>Info Privacy<br>Info Cookies<br>Termini e Condizioni di Vendita<br>Metodi di Pagamento<br>Spedizioni e Ritiri</div>
  <div class="col" style="left:898px"><h4 class="display">SERVIZI</h4>Preventivo Online<br>FAQs<br>Guide e Consigli<br>Cataloghi<br>Normative<br>Materiali</div>
  <div class="bottom"></div>
  <div class="copy">BORVELLO TRADE Srl © 2021 TUTTI I DIRITTI RISERVATI</div>
  <div class="social" aria-label="Canali social"><i></i><i></i><i></i><i></i></div>
</footer>

</body>
</html>
```